Real Estate Investment Company

Design Powerpoint slides are consistent with our logo, colors, and typeface. These Powerpoint slides will be used in all aspects of the business from live presentations to presentation decks available on a website or via email. Need to have different slide types created that allow for different types of slides such as cover pages, text heavy pages, image and chart heavy pages, multiple column pages, and mixed content pages.

Reason: to give additional time to get the design correct. I plan on making a selection in the next day or 2

Target Market(s)

Real Estate Investors

Industry/Entity Type

Investment

Other font styles liked:
• Consistent with logo

Requirements
Must have
• Our colors
• Our logo where possible
• Different slide designs of the same theme to allow for different types of slides such as cover pages, text heavy, picture heavy, and mixed content.
• Slides in both portrait and landscape orientation
Nice to have

```html
<!DOCTYPE html>
<html lang="en">
<head>
<meta charset="utf-8">
<title>Meet Our Team – Slide Layouts</title>
<link rel="stylesheet" href="https://fonts.googleapis.com/css2?family=Roboto:wght@400;500&family=Tinos:wght@400;700&family=Oswald:wght@500&display=swap">
<style>
:root{
  --navy:#29357f;
  --navy-band:rgba(41,53,127,.86);
  --mid-blue:#3d55a8;
  --title-blue:#2d5cab;
  --placeholder-blue:#2f6db3;
  --text-dark:#1f1f2a;
  --text-grey:#555a62;
  --page:#ececec;
  --white:#ffffff;
  --alert-red:#e3161b;
}
*{box-sizing:border-box;margin:0;padding:0}
html,body{width:1200px;height:685px;overflow:hidden;background:var(--page)}
body{position:relative;font-family:'Roboto',Arial,sans-serif}

.slide{position:absolute;width:740px;height:417px;background:var(--white);transform:scale(.8);transform-origin:0 0;overflow:hidden}
.slide--38{left:6px;top:8px}
.slide--39{left:602px;top:8px}
.slide--40{left:6px;top:346px}
.slide--41{left:602px;top:346px}

/* left photo column */
.hero-photo{position:absolute;left:0;width:196px;background:linear-gradient(180deg,#c4c6cc 0%,#ddd6c8 18%,#b9b1a3 38%,#9c958b 55%,#7e7a78 72%,#45444b 90%,#2f2e35 100%)}
.hero-photo--full{top:0;height:393px}
.hero-photo--lower{top:220px;height:173px;background:linear-gradient(180deg,#ddd6c8 0%,#b9b1a3 35%,#847f7b 65%,#35343b 100%)}
.hero-photo--under-band{top:138px;height:255px;background:linear-gradient(180deg,#ddd6c8 0%,#b9b1a3 30%,#8f8983 55%,#55535a 80%,#2f2e35 100%)}
.hero-caption{position:absolute;left:0;bottom:24px;width:196px;height:26px;background:rgba(41,53,127,.5);color:var(--white);font-size:9.5px;line-height:26px;padding-left:33px}
.title-band{position:absolute;left:0;top:28px;width:196px;height:60px;background:var(--navy-band);color:var(--white);font-family:'Tinos',serif;font-size:21px;line-height:60px;padding-left:30px}
.side-head{position:absolute;left:0;top:0;width:196px;height:138px;background:var(--navy)}
.side-head .title-band{top:76px;height:62px;line-height:62px;background:#3c4a95;padding-left:29px}

.page-title{position:absolute;left:32px;top:24px;font-family:'Tinos',serif;font-weight:700;font-size:25px;color:var(--navy)}
.page-title::after{content:"";position:absolute;left:0;top:36px;width:166px;height:3px;background:var(--navy)}

/* brand name */
.brand{position:absolute;display:flex;align-items:center;gap:5px;font-family:'Tinos',serif;font-size:8.5px;letter-spacing:.4px;color:var(--navy);text-transform:uppercase}
.brand__mark{width:11px;height:11px;border:1.5px solid currentColor}
.brand--corner{right:12px;top:30px}
.brand--light{left:20px;top:28px;color:var(--white);font-size:9.5px}

/* footer */
.footer{position:absolute;left:0;bottom:0;width:740px;height:24px;background:var(--navy);color:var(--white);font-family:'Tinos',serif;font-size:9px;line-height:24px;padding-left:12px}
.slide-num{position:absolute;right:0;bottom:0;width:60px;height:24px;background:var(--mid-blue);color:var(--white);font-size:9px;line-height:24px;text-align:center}
.slide-num b{font-size:12px;font-weight:400;margin-left:3px}

.before-tag{position:absolute;left:520px;top:56px;font-family:'Oswald',sans-serif;font-weight:500;font-size:50px;color:var(--alert-red);letter-spacing:1px}

/* members */
.member{position:absolute;display:flex;flex-direction:column;align-items:center;text-align:center;white-space:nowrap}
.avatar{border-radius:50%;border:3px solid var(--navy);background:radial-gradient(circle at 50% 42%,#f2dcc6 0%,#dcb596 24%,#a98065 46%,#8e8a90 66%,#c9d0da 100%)}
.avatar--empty{background:var(--placeholder-blue)}
.member__name{color:var(--text-dark);font-weight:500}
.member__role{color:var(--title-blue)}
.member__mail{color:var(--text-grey)}

.lead{position:absolute;display:flex;align-items:center;gap:14px}
.lead .avatar{width:90px;height:90px;border-width:4px}
.lead__name{font-size:15px;font-weight:500;color:var(--text-dark)}
.lead__role{font-size:12px;color:var(--title-blue);margin-top:3px}
.lead__mail{font-size:11.5px;color:var(--text-grey);margin-top:3px}

.team-a .member{width:180px;margin-left:-90px}
.team-a .avatar{width:66px;height:66px}
.team-a .member__name{font-size:13px;margin-top:8px}
.team-a .member__role{font-size:10.5px;margin-top:1px}
.team-a .member__mail{font-size:10.5px;margin-top:1px}

.team-b .member{width:130px;margin-left:-65px}
.team-b .avatar{width:76px;height:76px}
.team-b .member__name{font-size:12.5px;margin-top:4px}
.team-b .member__role{font-size:8.5px;margin-top:2px}
.team-b .member__mail{font-size:7.5px;margin-top:2px}

.team-c .member{width:140px;margin-left:-70px}
.team-c .avatar{width:92px;height:92px}
.team-c .member__name{font-family:'Tinos',serif;font-weight:400;font-size:14.5px;margin-top:6px}
.team-c .member__role{font-size:10.5px;margin-top:1px}
.team-c .member__mail{font-size:8.5px;margin-top:2px}

.team-d .member{width:132px;margin-left:-66px}
.tile{position:relative;width:100px;height:98px;border:2px solid var(--navy);background:linear-gradient(180deg,#dfe4ea 0%,#eed3b9 30%,#c99f80 55%,#8f7566 75%,#6e7482 100%)}
.tile--empty{background:var(--placeholder-blue)}
.tile__name{position:absolute;left:0;right:0;bottom:0;height:20px;background:rgba(41,53,127,.6);color:var(--white);font-family:'Tinos',serif;font-size:11px;line-height:20px}
.team-d .member__role{font-size:10.5px;margin-top:3px}
.team-d .member__mail{font-size:8.5px;margin-top:1px}
</style>
</head>
<body>

<section class="slide slide--38 team-a">
  <div class="hero-photo hero-photo--full" role="img" aria-label="Company president standing outside a stone building with the office dog"></div>
  <div class="title-band">Meet Our Team</div>
  <div class="hero-caption">Martin with Our Mascot, Rosie</div>
  <div class="brand brand--corner"><span class="brand__mark"></span>Cedar Peak Management</div>
  <div class="lead" style="left:224px;top:30px">
    <div class="avatar" role="img" aria-label="Portrait of Martin Hale"></div>
    <div><div class="lead__name">Martin Hale</div><div class="lead__role">President</div><div class="lead__mail">martin@haleproperties.com</div></div>
  </div>
  <div class="before-tag">BEFORE</div>
  <div class="member" style="left:315px;top:120px"><div class="avatar" role="img" aria-label="Portrait of Nora Hale"></div><div class="member__name">Nora Hale</div><div class="member__role">New York Asset Manager</div><div class="member__mail">nora@haleproperties.com</div></div>
  <div class="member" style="left:482px;top:120px"><div class="avatar" role="img" aria-label="Portrait of Laura Pike"></div><div class="member__name">Laura Pike</div><div class="member__role">Position Goes Here</div><div class="member__mail">laura@haleproperties.com</div></div>
  <div class="member" style="left:647px;top:120px"><div class="avatar" role="img" aria-label="Portrait of Dana Kerr"></div><div class="member__name">Dana Kerr</div><div class="member__role">Position Goes Here</div><div class="member__mail">dkerrwp@mailbox.com</div></div>
  <div class="member" style="left:315px;top:250px"><div class="avatar" role="img" aria-label="Portrait of Molly Grant"></div><div class="member__name">Molly Grant</div><div class="member__role">Administrative Assistant</div><div class="member__mail">molly@haleproperties.com</div></div>
  <div class="member" style="left:482px;top:250px"><div class="avatar" role="img" aria-label="Portrait of Ben Porter"></div><div class="member__name">Ben Porter</div><div class="member__role">Director of Finance</div><div class="member__mail">ben@haleproperties.com</div></div>
  <div class="member" style="left:647px;top:250px"><div class="avatar" role="img" aria-label="Portrait of Ruth Ames"></div><div class="member__name">Ruth Ames</div><div class="member__role">Administrative Assistant</div><div class="member__mail">ruth@haleproperties.com</div></div>
  <footer class="footer">CEDAR PEAK MANAGEMENT CORPORATION © 2016. All rights reserved.</footer>
  <div class="slide-num">Slide<b>38</b></div>
</section>

<section class="slide slide--39 team-b">
  <div class="hero-photo hero-photo--full" role="img" aria-label="Company president standing outside a stone building with the office dog"></div>
  <div class="title-band">Meet Our Team</div>
  <div class="hero-caption">Martin with Our Mascot, Rosie</div>
  <div class="brand brand--corner"><span class="brand__mark"></span>Cedar Peak Management</div>
  <div class="lead" style="left:234px;top:18px">
    <div class="avatar" role="img" aria-label="Portrait of Martin Hale"></div>
    <div><div class="lead__name">Martin Hale</div><div class="lead__role">President</div><div class="lead__mail">martin@haleproperties.com</div></div>
  </div>
  <div class="member" style="left:282px;top:121px"><div class="avatar" role="img" aria-label="Portrait of Nora Hale"></div><div class="member__name">Nora Hale</div><div class="member__role">New York Asset Manager</div><div class="member__mail">nora@haleproperties.com</div></div>
  <div class="member" style="left:409px;top:121px"><div class="avatar" role="img" aria-label="Portrait of Laura Pike"></div><div class="member__name">Laura Pike</div><div class="member__role">Position Goes Here</div><div class="member__mail">laura@haleproperties.com</div></div>
  <div class="member" style="left:531px;top:121px"><div class="avatar" role="img" aria-label="Portrait of Dana Kerr"></div><div class="member__name">Dana Kerr</div><div class="member__role">Position Goes Here</div><div class="member__mail">dkerrwp@mailbox.com</div></div>
  <div class="member" style="left:657px;top:121px"><div class="avatar avatar--empty" role="img" aria-label="Placeholder portrait silhouette"></div><div class="member__name">Dana Kerr</div><div class="member__role">Position Goes Here</div><div class="member__mail">dkerrwp@mailbox.com</div></div>
  <div class="member" style="left:282px;top:251px"><div class="avatar" role="img" aria-label="Portrait of Molly Grant"></div><div class="member__name">Molly Grant</div><div class="member__role">Administrative Assistant</div><div class="member__mail">molly@haleproperties.com</div></div>
  <div class="member" style="left:409px;top:251px"><div class="avatar" role="img" aria-label="Portrait of Ben Porter"></div><div class="member__name">Ben Porter</div><div class="member__role">Director of Finance</div><div class="member__mail">ben@haleproperties.com</div></div>
  <div class="member" style="left:531px;top:251px"><div class="avatar" role="img" aria-label="Portrait of Ruth Ames"></div><div class="member__name">Ruth Ames</div><div class="member__role">Administrative Assistant</div><div class="member__mail">ruth@haleproperties.com</div></div>
  <div class="member" style="left:657px;top:251px"><div class="avatar avatar--empty" role="img" aria-label="Placeholder portrait silhouette"></div><div class="member__name">Ruth Ames</div><div class="member__role">Administrative Assistant</div><div class="member__mail">ruth@haleproperties.com</div></div>
  <footer class="footer">CEDAR PEAK MANAGEMENT CORPORATION © 2016. All rights reserved.</footer>
  <div class="slide-num">Slide<b>39</b></div>
</section>

<section class="slide slide--40 team-c">
  <h1 class="page-title">Meet Our Team</h1>
  <div class="brand brand--corner"><span class="brand__mark"></span>Cedar Peak Management</div>
  <div class="hero-photo hero-photo--lower" role="img" aria-label="Company president standing outside a stone building with the office dog"></div>
  <div class="hero-caption">Martin with Our Mascot, Rosie</div>
  <div class="member" style="left:107px;top:73px"><div class="avatar" role="img" aria-label="Portrait of Martin Hale"></div><div class="member__name">Martin Hale</div><div class="member__role">President</div><div class="member__mail">martin@haleproperties.com</div></div>
  <div class="member" style="left:273px;top:73px"><div class="avatar" role="img" aria-label="Portrait of Nora Hale"></div><div class="member__name">Nora Hale</div><div class="member__role">New York Asset Manager</div><div class="member__mail">nora@haleproperties.com</div></div>
  <div class="member" style="left:405px;top:73px"><div class="avatar" role="img" aria-label="Portrait of Laura Pike"></div><div class="member__name">Laura Pike</div><div class="member__role">Position Goes Here</div><div class="member__mail">laura@haleproperties.com</div></div>
  <div class="member" style="left:536px;top:73px"><div class="avatar" role="img" aria-label="Portrait of Dana Kerr"></div><div class="member__name">Dana Kerr</div><div class="member__role">Position Goes Here</div><div class="member__mail">dkerrwp@mailbox.com</div></div>
  <div class="member" style="left:667px;top:73px"><div class="avatar avatar--empty" role="img" aria-label="Placeholder portrait silhouette"></div><div class="member__name">Additional Person</div><div class="member__role">Position Goes Here</div><div class="member__mail">name@haleproperties.com</div></div>
  <div class="member" style="left:273px;top:228px"><div class="avatar" role="img" aria-label="Portrait of Molly Grant"></div><div class="member__name">Molly Grant</div><div class="member__role">Administrative Assistant</div><div class="member__mail">molly@haleproperties.com</div></div>
  <div class="member" style="left:405px;top:228px"><div class="avatar" role="img" aria-label="Portrait of Ben Porter"></div><div class="member__name">Ben Porter</div><div class="member__role">Director of Finance</div><div class="member__mail">ben@haleproperties.com</div></div>
  <div class="member" style="left:536px;top:228px"><div class="avatar" role="img" aria-label="Portrait of Ruth Ames"></div><div class="member__name">Ruth Ames</div><div class="member__role">Administrative Assistant</div><div class="member__mail">ruth@haleproperties.com</div></div>
  <div class="member" style="left:667px;top:228px"><div class="avatar avatar--empty" role="img" aria-label="Placeholder portrait silhouette"></div><div class="member__name">Additional Person</div><div class="member__role">Position Goes Here</div><div class="member__mail">name@haleproperties.com</div></div>
  <footer class="footer">CEDAR PEAK MANAGEMENT CORPORATION © 2016. All rights reserved.</footer>
  <div class="slide-num">Slide<b>40</b></div>
</section>

<section class="slide slide--41 team-d">
  <div class="side-head">
    <div class="brand brand--light"><span class="brand__mark"></span>Cedar Peak Management</div>
    <div class="title-band">Meet Our Team</div>
  </div>
  <div class="hero-photo hero-photo--under-band" role="img" aria-label="Company president standing outside a stone building with the office dog"></div>
  <div class="hero-caption">Martin with Our Mascot, Rosie</div>
  <div class="member" style="left:273px;top:11px"><div class="tile" role="img" aria-label="Portrait of Martin Hale"><span class="tile__name">Martin Hale</span></div><div class="member__role">President</div><div class="member__mail">martin@haleproperties.com</div></div>
  <div class="member" style="left:401px;top:11px"><div class="tile" role="img" aria-label="Portrait of Nora Hale"><span class="tile__name">Nora Hale</span></div><div class="member__role">New York Asset Manager</div><div class="member__mail">nora@haleproperties.com</div></div>
  <div class="member" style="left:530px;top:11px"><div class="tile" role="img" aria-label="Portrait of Laura Pike"><span class="tile__name">Laura Pike</span></div><div class="member__role">Position Goes Here</div><div class="member__mail">laura@haleproperties.com</div></div>
  <div class="member" style="left:660px;top:11px"><div class="tile" role="img" aria-label="Portrait of Dana Kerr"><span class="tile__name">Dana Kerr</span></div><div class="member__role">Position Goes Here</div><div class="member__mail">dkerrwp@mailbox.com</div></div>
  <div class="member" style="left:273px;top:137px"><div class="tile" role="img" aria-label="Portrait of Molly Grant"><span class="tile__name">Molly Grant</span></div><div class="member__role">Administrative Assistant</div><div class="member__mail">molly@haleproperties.com</div></div>
  <div class="member" style="left:401px;top:137px"><div class="tile" role="img" aria-label="Portrait of Ben Porter"><span class="tile__name">Ben Porter</span></div><div class="member__role">Director of Finance</div><div class="member__mail">ben@haleproperties.com</div></div>
  <div class="member" style="left:530px;top:137px"><div class="tile" role="img" aria-label="Portrait of Ruth Ames"><span class="tile__name">Ruth Ames</span></div><div class="member__role">Administrative Assistant</div><div class="member__mail">ruth@haleproperties.com</div></div>
  <div class="member" style="left:660px;top:137px"><div class="tile tile--empty" role="img" aria-label="Placeholder portrait silhouette"><span class="tile__name">John Smith</span></div><div class="member__role">Position Goes Here</div><div class="member__mail">name@haleproperties.com</div></div>
  <div class="member" style="left:273px;top:263px"><div class="tile tile--empty" role="img" aria-label="Placeholder portrait silhouette"><span class="tile__name">Jane Smith</span></div><div class="member__role">Position Goes Here</div><div class="member__mail">name@haleproperties.com</div></div>
  <div class="member" style="left:401px;top:263px"><div class="tile tile--empty" role="img" aria-label="Placeholder portrait silhouette"><span class="tile__name">John Smith</span></div><div class="member__role">Position Goes Here</div><div class="member__mail">name@haleproperties.com</div></div>
  <div class="member" style="left:530px;top:263px"><div class="tile tile--empty" role="img" aria-label="Placeholder portrait silhouette"><span class="tile__name">Jane Smith</span></div><div class="member__role">Position Goes Here</div><div class="member__mail">name@haleproperties.com</div></div>
  <footer class="footer">CEDAR PEAK MANAGEMENT CORPORATION © 2016. All rights reserved.</footer>
  <div class="slide-num">Slide<b>41</b></div>
</section>

</body>
</html>
```